Business Card Design

I'm a young beekeeper (22 years old) just starting out. I own and run 80 hives and would like to eventually build up to 1000. My aim is to run it in tandem with our family farm that is currently running sheep and beef. Unlike a number of honey companies on the East Coast (or the North Island, NZ) I am local and will expand onto the lease blocks that our family is also leasing. I want a simple plain logo/photo. The designer may wish to use one of the photos as a background outline or however they chose. The mountain is Aorangi and our farm borders one side of it.

Target Market(s)

From local land owners to wholesale honey buyers

Industry/Entity Type

Farm

Contact Information for Business Card

Pekeriu Honey
Manager Owner Manaia Brooks
email pekeriuhoney@tuimailbox.co.nz
mobile 0217394461

Requirements
Must have
• The details submitted. The brand Pekeriu Honey to be the main feature. The other details can be smaller.
Should not have
• Must not include a picture of a bee or hive. Use a modern font. Don't use koru but may incorporate poutama.

```html
<!DOCTYPE html>
<html lang="en">
<head>
<meta charset="utf-8">
<title>Pekeriu Honey – Business Card</title>
<link rel="stylesheet" href="https://fonts.googleapis.com/css2?family=Original+Surfer&family=Sniglet&family=Cabin:wght@500&display=swap">
<style>
  :root {
    --frame-dark: #2f2a07;
    --frame-gold: #b4860d;
    --corner-dark: #3a3208;
    --sky-pale: #eef3ea;
    --sky-blue: #b9dfe6;
    --mountain: #4d6770;
    --forest: #3f5a3a;
    --ground: #7d7a45;
    --ground-light: #a59a60;
    --ink: #141414;
    --paper: #ffffff;
  }
  html, body {
    margin: 0;
    padding: 0;
    width: 1200px;
    height: 730px;
    overflow: hidden;
    background: #ffffff;
  }
  .card {
    position: relative;
    width: 1200px;
    height: 730px;
    background: var(--frame-dark);
    overflow: hidden;
  }
  .card__gold-rule {
    position: absolute;
    left: 24px; top: 24px; right: 24px; bottom: 24px;
    border: 9px solid var(--frame-gold);
  }
  .card__landscape {
    position: absolute;
    left: 33px; top: 33px; right: 33px; bottom: 33px;
    background:
      linear-gradient(180deg,
        var(--sky-pale) 0%,
        var(--sky-blue) 22%,
        var(--mountain) 36%,
        var(--forest) 55%,
        var(--ground) 70%,
        var(--ground-light) 82%,
        var(--ground) 100%);
  }
  .card__corners {
    position: absolute;
    inset: 0;
  }
  .card__text {
    position: absolute;
    left: 0; right: 0;
    margin: 0;
    text-align: center;
    line-height: 1;
    white-space: nowrap;
  }
  .brand-name {
    top: 62px;
    font-family: "Original Surfer", sans-serif;
    font-size: 148px;
    color: var(--ink);
    letter-spacing: 2px;
  }
  .person-name {
    top: 228px;
    font-family: "Original Surfer", sans-serif;
    font-size: 86px;
    color: var(--ink);
  }
  .person-role {
    top: 328px;
    font-family: "Cabin", sans-serif;
    font-weight: 500;
    font-size: 33px;
    color: var(--ink);
  }
  .person-phone {
    top: 378px;
    font-family: "Cabin", sans-serif;
    font-weight: 500;
    font-size: 39px;
    color: var(--ink);
    letter-spacing: 1px;
  }
  .contact-email {
    top: 650px;
    font-family: "Sniglet", sans-serif;
    font-size: 37px;
    color: var(--paper);
  }
</style>
</head>
<body>
  <main class="card">
    <div class="card__gold-rule"></div>
    <div class="card__landscape" role="img" aria-label="Photograph of the mountain rising above native forest and open grassy farmland, with a faint poutama-style pattern over the sky"></div>

    <svg class="card__corners" width="1200" height="730" viewBox="0 0 1200 730" aria-hidden="true">
      <g fill="var(--corner-dark)" stroke="var(--frame-gold)" stroke-width="9">
        <circle cx="0" cy="0" r="135"/>
        <circle cx="1200" cy="0" r="135"/>
        <circle cx="0" cy="730" r="135"/>
        <circle cx="1200" cy="730" r="135"/>
      </g>
    </svg>

    <h1 class="card__text brand-name">Pekeriu Honey</h1>
    <p class="card__text person-name">Manaia Brooks</p>
    <p class="card__text person-role">Manager Owner</p>
    <p class="card__text person-phone">0217394461</p>
    <p class="card__text contact-email">email: pekeriuhoney@tuimailbox.co.nz</p>
  </main>
</body>
</html>
```